lighting products eshop web site

We need a brand new ecommerce website (only psd files for the layout) , that will sell professional lighting products in Greek territory.
Please check the sister site www.lampivo.gr to get an idea of the products, they will be similar, actually like the products under the menu category "ΕΠΑΓΓΕΛΜΑΤΙΚΑ".
We would like the same philosophy as far as concern the menu structure, namely the menu categories/subcategories shall be actually the products
categories/subcategories, however the menu items shall be presented in a different, more sophisticated way. As far as concern the website layout, we need a minimal, elegant
and contemporary approach that will highlight the products in a perfect manner. We prefer the white color as the main website (background) color and discrete use of brand logo colors.
That is the main idea, awaiting your personal proposal according to the aforementioned requirements
Technically speaking we use bootstrap framework in terms of design meaning 12cols with max width 1170px.
The website will be a joomla - virtuemart website

For images please use some from lumento.gr
For text use any text - just to show me the space.

Industry/Entity Type

It Professional

Number of Pages Required

3 page

Font styles to use
Sans Serif

Colors
00a990
ec1f27

Requirements
Must have
• I need 4 psd pages for the website
• 1. Start page
• 2. Category page
• 3. Product details page
• 4. blog page
Nice to have
• leave designer to choose the best

```html
<!DOCTYPE html>
<html lang="en">
<head>
<meta charset="utf-8">
<title>Lumento – Category</title>
<link href="https://fonts.googleapis.com/css2?family=Roboto:wght@300;400;500&display=swap" rel="stylesheet">
<style>
:root{
  --green:#00a990;
  --red:#ec1f27;
  --ink:#333;
  --muted:#777;
  --line:#e3e3e3;
  --soft:#f3f3f3;
  --white:#fff;
}
*{box-sizing:border-box;margin:0;padding:0}
html,body{width:1200px;height:2528px;overflow:hidden;background:var(--white)}
body{font-family:'Roboto',Arial,sans-serif;color:var(--ink);position:relative;font-size:13px}
.abs{position:absolute}
a{color:inherit;text-decoration:none}

/* top bar */
.topbar{left:0;top:0;width:1200px;height:35px;border-bottom:1px solid var(--line)}
.lang{left:88px;top:0;height:35px;width:105px;background:var(--soft);font-size:10px;display:flex;align-items:center;gap:6px;padding-left:12px}
.lang .flag{width:16px;height:11px;background:#3a4a9a}
.welcome{left:211px;top:10px;font-size:12px;color:var(--muted)}
.welcome a{color:var(--green)}
.toplinks{top:10px;font-size:12px;color:var(--muted)}
.social{top:2px;width:28px;height:28px}

/* header */
.logo{left:88px;top:62px;font-size:40px;font-weight:300;letter-spacing:10px;color:var(--red)}
.search{left:666px;top:63px;width:225px;height:39px;background:var(--soft);border:1px solid var(--line);font-size:11px;padding:12px 14px;color:#555}
.search svg{position:absolute;right:10px;top:11px}
.hicon{top:72px}
.cart{left:994px;top:66px;width:116px;height:35px;background:var(--red);color:#fff;font-size:12px;display:flex;align-items:center;justify-content:center;gap:8px}

/* navigation */
.nav{left:0;top:134px;width:1200px;height:42px;background:var(--green)}
.nav span{position:absolute;top:0;height:42px;line-height:42px;color:#fff;font-size:12px;font-weight:500}
.nav .active{background:var(--red);padding:0 20px}
.nav span::after{content:" ▾";font-size:9px}

/* page title */
.pagehead{left:0;top:176px;width:1200px;height:93px;border-bottom:1px solid var(--line)}
.pagehead h1{position:absolute;left:88px;top:36px;font-size:21px;font-weight:400}
.crumbs{position:absolute;right:90px;top:40px;font-size:12px}
.crumbs em{color:var(--red);font-style:normal}

/* sidebar */
.side-title{left:88px;font-size:16px;color:#444;border-bottom:1px solid var(--line);width:239px;padding-bottom:10px}
.quest-input{left:90px;top:342px;width:237px;height:41px;border:1px solid #ddd}
.quest-btn{left:90px;top:389px;width:237px;height:41px;background:var(--red);color:#fff;font-size:14px;text-align:center;line-height:41px}
.filters{left:88px;top:491px;list-style:none;font-size:10.5px}
.filters li{height:23px;display:flex;align-items:center;gap:11px}
.filters li::before{content:"";width:11px;height:11px;border:1px solid #ccc}
.price-label{left:88px;top:855px;font-size:12px;color:#555}
.price-in{top:880px;width:80px;height:35px;border:1px solid #ddd}
.price-btn{left:251px;top:880px;width:76px;height:35px;background:var(--green)}
.slider{left:103px;top:939px;width:205px;height:2px;background:#ccc}
.clear{left:88px;top:960px;font-size:12px;color:var(--red)}
.best{left:88px;width:239px;height:84px;border-bottom:1px solid var(--line);display:flex;gap:18px;align-items:center}
.best .thumb{width:64px;height:64px;background:#eef0f2}
.best p{font-size:11px;line-height:19px}
.best .stars{color:#ccc;font-size:10px;letter-spacing:1px}
.best .cost{color:var(--red)}
.cats{left:88px;top:1352px;width:200px;list-style:none;font-size:11px}
.cats li{height:30px;line-height:30px;display:flex;justify-content:space-between}
.cats li.sub{padding-left:34px;color:#555}
.cats li.open{color:var(--red)}
.callbox{left:89px;top:1694px;width:233px;height:232px;background:var(--red);color:#fff;text-align:center}
.callbox .name{margin-top:22px;font-size:32px;font-weight:300;letter-spacing:5px}
.callbox svg{margin-top:18px}
.callbox .tel{margin-top:14px;font-size:30px;font-weight:500;letter-spacing:1px}

/* content */
.cat-title{left:369px;top:300px;font-size:16px;font-weight:500}
.select{top:296px;height:28px;border:1px solid #ddd;font-size:11px;padding:7px 10px}
.view{left:1000px;top:303px;font-size:11px}
.vbtn{top:300px;width:23px;height:23px}
.results{left:369px;font-size:11px;color:#555;display:flex;align-items:center;gap:10px}
.results .show{width:45px;height:27px;border:1px solid #ddd;padding:6px 10px}
.card{width:240px;height:282px;border:1px solid var(--line);text-align:center}
.card .img{width:196px;height:148px;margin:22px auto 0;background:linear-gradient(#f7f7f7,#ececec)}
.card h3{font-size:16px;font-weight:400;margin-top:22px;white-space:nowrap}
.card .price{color:var(--red);font-size:17px;margin-top:8px}
.card .add{border-top:1px solid var(--line);margin:8px 16px 0;padding-top:10px;font-size:13px}

/* manufacturers */
.mf-title{left:0;top:1960px;width:1200px;text-align:center;font-size:28px;font-weight:300;letter-spacing:1px}
.mf-rule{left:578px;top:2006px;width:44px;height:2px;background:var(--red)}
.mf{top:2024px;width:165px;height:77px;border:1px solid var(--line);display:flex;align-items:center;justify-content:center;font-size:20px;font-weight:500;color:#444}

/* newsletter */
.news{left:0;top:2145px;width:1200px;height:81px;background:var(--green);color:#fff}
.news h2{position:absolute;left:88px;top:18px;font-size:20px;font-weight:400}
.news p{position:absolute;left:88px;top:46px;font-size:12px}
.news .field{position:absolute;left:627px;top:20px;width:352px;height:41px;background:#fff;color:#999;font-size:12px;padding:13px 25px}
.news .btn{position:absolute;left:979px;top:20px;width:132px;height:41px;background:var(--red);font-size:14px;text-align:center;line-height:41px}

/* footer */
.fcol{top:2265px}
.fcol h4{font-size:16px;font-weight:400;margin-bottom:10px}
.fcol p{font-size:12px;line-height:21px;width:290px}
.fcol ul{list-style:none;font-size:12px}
.fcol li{height:31px;line-height:21px}
.fcol li::before{content:"›";color:var(--red);font-size:18px;margin-right:10px}
.fline{left:88px;top:2482px;width:1024px;height:1px;background:var(--line)}
.copy{left:0;top:2499px;width:1200px;text-align:center;font-size:12px}
.totop{left:1117px;top:2467px;width:34px;height:34px;background:var(--red)}
</style>
</head>
<body>

<!-- top bar -->
<div class="abs topbar"></div>
<div class="abs lang"><span class="flag"></span>ENGLISH ▾</div>
<div class="abs welcome">Welcome <a>Login</a> Forgotten &nbsp;or <a>Create an Account</a></div>
<div class="abs toplinks" style="left:787px">My account</div>
<div class="abs toplinks" style="left:876px">Orders</div>
<div class="abs toplinks" style="left:939px">Shopping basket</div>
<div class="abs social" style="left:1046px;background:#3b5998"></div>
<div class="abs social" style="left:1080px;background:#1da1f2"></div>

<!-- header -->
<div class="abs logo">LUMENTO</div>
<div class="abs search">Search Our Store
  <svg width="16" height="16" viewBox="0 0 16 16"><circle cx="7" cy="7" r="5" fill="none" stroke="#777" stroke-width="1.5"/><line x1="11" y1="11" x2="15" y2="15" stroke="#777" stroke-width="1.5"/></svg>
</div>
<svg class="abs hicon" style="left:922px" width="24" height="22" viewBox="0 0 24 22"><path d="M12 19 L3 10 A5 5 0 0 1 12 4 A5 5 0 0 1 21 10 Z" fill="none" stroke="#888" stroke-width="1.5"/></svg>
<svg class="abs hicon" style="left:956px" width="22" height="22" viewBox="0 0 22 22"><rect x="3" y="2" width="11" height="16" fill="none" stroke="#888" stroke-width="1.5"/><rect x="9" y="7" width="10" height="13" fill="#fff" stroke="#888" stroke-width="1.5"/></svg>
<div class="abs cart">
  <svg width="16" height="14" viewBox="0 0 16 14"><path d="M1 1h3l2 8h8l2-6H5" fill="none" stroke="#fff" stroke-width="1.5"/><circle cx="7" cy="12" r="1.3" fill="#fff"/><circle cx="13" cy="12" r="1.3" fill="#fff"/></svg>
  CART ( 0 )
</div>

<!-- navigation -->
<nav class="abs nav">
  <span class="active" style="left:148px">HANGING</span>
  <span style="left:278px">ROOF</span>
  <span style="left:362px">WALL</span>
  <span style="left:447px">FLOOR</span>
  <span style="left:539px">SPOT</span>
  <span style="left:623px">OUTDOOR</span>
  <span style="left:733px">FANS</span>
  <span style="left:817px">PROFESSIONAL</span>
  <span style="left:960px">COMPANIES</span>
</nav>

<!-- page heading -->
<div class="abs pagehead">
  <h1>Category</h1>
  <div class="crumbs"><span style="color:var(--green)">⌂</span> Home / <em>Category</em></div>
</div>

<!-- sidebar -->
<div class="abs side-title" style="top:300px">Quest</div>
<div class="abs quest-input"></div>
<div class="abs quest-btn">Quest</div>

<div class="abs side-title" style="top:452px;left:90px">Search Filters</div>
<ul class="abs filters">
  <li>ARCO LIGHT</li><li>ELDRA (7)</li><li>FANWELL</li><li>FARIO</li><li>Gaveo</li>
  <li>HOMELUME(3)</li><li>HOLTEN</li><li>IDRA LUX (1)</li><li>INLUMA</li><li>LUMEN</li>
  <li>NOVA LINEA</li><li>SPOTIVA</li><li>VOLTAC</li><li>VIORA (1)</li><li>ZAMORA LIGHTS</li>
</ul>
<div class="abs price-label">› &nbsp;Price<span style="position:absolute;left:80px;white-space:nowrap">€ &nbsp;up to</span></div>
<div class="abs price-in" style="left:88px"></div>
<div class="abs price-in" style="left:168px"></div>
<div class="abs price-btn"><svg width="76" height="35" viewBox="0 0 76 35"><circle cx="37" cy="16" r="5" fill="none" stroke="#fff" stroke-width="2"/><line x1="41" y1="20" x2="44" y2="23" stroke="#fff" stroke-width="2"/></svg></div>
<div class="abs slider"></div>
<svg class="abs" style="left:96px;top:933px" width="220" height="14"><circle cx="8" cy="7" r="7" fill="#ec1f27"/><circle cx="211" cy="7" r="7" fill="#aaa"/></svg>
<div class="abs clear">All Clearance</div>

<div class="abs side-title" style="top:1000px;border:0">Bestsellers</div>
<div class="abs best" style="top:1035px"><div class="thumb" role="img" aria-label="White pendant lamp"></div><p>HALORA<br><span class="stars">☆☆☆☆☆</span><br><span class="cost">158,50 €</span></p></div>
<div class="abs best" style="top:1119px"><div class="thumb" role="img" aria-label="Black outdoor spike spotlight"></div><p>ORBIS KX4<br><span class="stars">☆☆☆☆☆</span><br><span class="cost">29,24 €</span></p></div>
<div class="abs best" style="top:1203px;border:0"><div class="thumb" role="img" aria-label="Multi-light bar pendant"></div><p>RIVANO<br><span class="stars">☆☆☆☆☆</span><br><span class="cost">207,87 €</span></p></div>

<div class="abs side-title" style="top:1314px">Categories</div>
<ul class="abs cats">
  <li class="open"><span>FANS</span><span>–</span></li>
  <li class="sub">ACCESSORIES</li>
  <li class="sub">WITH LIGHT</li>
  <li class="sub">WITHOUT LIGHT</li>
  <li><span>FLOOR</span><span>+</span></li>
  <li><span>OUTDOOR</span><span>+</span></li>
  <li><span>PROFESSIONAL</span><span>+</span></li>
  <li><span>WALL</span><span>+</span></li>
  <li><span>PENDANT</span><span>+</span></li>
  <li><span>ROOF</span><span>+</span></li>
  <li><span>SPOT</span><span>+</span></li>
</ul>

<div class="abs callbox">
  <div class="name">LUMENTO</div>
  <svg width="64" height="56" viewBox="0 0 64 56"><path d="M4 16 Q32 0 60 16 L56 24 L46 20 L46 14 Q32 10 18 14 L18 20 L8 24 Z" fill="#111"/><path d="M14 26 L50 26 L58 52 L6 52 Z" fill="#111"/><circle cx="32" cy="39" r="8" fill="#ec1f27"/></svg>
  <div class="tel">800 12345 67</div>
</div>

<!-- content -->
<div class="abs cat-title">ACCESSORIES</div>
<div class="abs select" style="left:727px;width:99px">Orders +/- &nbsp;▾</div>
<div class="abs select" style="left:833px;width:149px">Select Manufacture &nbsp;▾</div>
<div class="abs view">View: Grid</div>
<div class="abs vbtn" style="left:1061px;background:var(--red)"></div>
<div class="abs vbtn" style="left:1088px;background:#222"></div>
<div class="abs results" style="top:340px">Results 1-6 of 6 <span>show:</span><span class="show">9 ▾</span></div>

<div class="abs card" style="left:369px;top:388px"><div class="img" role="img" aria-label="White handheld fan remote control"></div><h3>KIT REMOTE CONTROL</h3><div class="price">75,00 €</div><div class="add">Add to Cart</div></div>
<div class="abs card" style="left:622px;top:388px"><div class="img" role="img" aria-label="Fan remote control with display"></div><h3>KIT REMOTE CONTROL ....</h3><div class="price">88,00 €</div><div class="add">Add to Cart</div></div>
<div class="abs card" style="left:871px;top:388px"><div class="img" role="img" aria-label="Slim fan remote control"></div><h3>BREEZE REMOTE CONTROL</h3><div class="price">181,00 €</div><div class="add">Add to Cart</div></div>
<div class="abs card" style="left:369px;top:683px"><div class="img" role="img" aria-label="Brass pull chain accessory"></div><h3>300MM. CHAIN ACCESSORY</h3><div class="price">30,00 €</div><div class="add">Add to Cart</div></div>
<div class="abs card" style="left:622px;top:683px"><div class="img" role="img" aria-label="Wall mounted fan speed control"></div><h3>WALL CONTROL WITH 3...</h3><div class="price">181,00 €</div><div class="add">Add to Cart</div></div>
<div class="abs card" style="left:871px;top:683px"><div class="img" role="img" aria-label="Clear glass light kit for fan"></div><h3>LIGHT KIT FOR MINI-AIRFAN</h3><div class="price">43,00 €</div><div class="add">Add to Cart</div></div>

<div class="abs results" style="top:991px">Results 1-6 of 6 <span>show:</span><span class="show">9 ▾</span><span>Items Per Page</span></div>

<!-- manufacturers -->
<div class="abs mf-title">MANUFACTURERS</div>
<div class="abs mf-rule"></div>
<div class="abs mf" style="left:88px">ELDRA</div>
<div class="abs mf" style="left:260px">INLUMA</div>
<div class="abs mf" style="left:431px">IDRA LUX</div>
<div class="abs mf" style="left:602px">HOLTEN</div>
<div class="abs mf" style="left:773px">GALVEN</div>
<div class="abs mf" style="left:945px">VOLTAC</div>

<!-- newsletter -->
<section class="abs news">
  <h2>SUBSCRIBE TO OUR NEWSLETTER</h2>
  <p>to MATHENOUN first for our special offers!</p>
  <div class="field">Enter your email address</div>
  <div class="btn">SUBSCRIBE</div>
</section>

<!-- footer -->
<div class="abs fcol" style="left:88px"><h4>ABOUT</h4><p>The LUMENTO welcomes you to bright electronic space. Thousands of lights constantly growing and updated selected to illuminate your space at the best prices.</p></div>
<div class="abs fcol" style="left:453px"><h4>LUMENTO</h4><ul><li>The company</li><li>The shop</li><li>Cooperating companies</li><li>Data protection</li><li>Terms of use</li></ul></div>
<div class="abs fcol" style="left:711px"><h4>SERVICES</h4><ul><li>Connection</li><li>record</li><li>Wish List</li><li>Basket</li><li>Communication</li></ul></div>
<div class="abs fcol" style="left:942px"><h4>INFORMATION</h4><ul><li>Payment methods</li><li>Shipping methods</li><li>Return policy</li><li>Returns form</li></ul></div>
<div class="abs fline"></div>
<div class="abs copy">Copyright 2016 lumento.gr.</div>
<div class="abs totop"><svg width="34" height="34" viewBox="0 0 34 34"><path d="M12 19 L17 14 L22 19" fill="none" stroke="#fff" stroke-width="2"/></svg></div>

</body>
</html>
```